Brightwell Surface Care - Business Card Design

Use company logo and design a new business card. We are looking for a front and back design. The back should be a dark purple background. We want the back to show cartoon-like soap bubbles chasing mildew cartoon shaped figures. This gives the idea that Brightwell Surface Care provides exterior washing services that work. No mildew stands a chance when Brightwell Surface Care shows up to work. The mildew cartoon images should be green in color, have eyes, and look scared of the bubbles. The bubbles should be light blue in color and have eyes that looked excited to be there.
We will advertise on Mingleport and Pixelvine. These Mingleport and Pixelvine icons should be somewhere on the card.

```html
<!DOCTYPE html>
<html lang="en">
<head>
<meta charset="utf-8">
<title>Brightwell Surface Care – Business Card</title>
<link rel="stylesheet" href="https://fonts.googleapis.com/css2?family=Quicksand:wght@500;700&display=swap">
<style>
  :root{
    --backdrop:#4a4a4d;
    --card-white:#ffffff;
    --brand-purple:#3b1f62;
    --foam-blue:#94dcfa;
    --bubble-blue:#bfe9fb;
    --germ-green:#8cc63f;
    --text-light:#ffffff;
    --accent-blue:#9fd9f5;
  }
  *{box-sizing:border-box;margin:0;padding:0}
  html,body{width:1200px;height:1200px;overflow:hidden}
  body{background:var(--backdrop);font-family:"Quicksand",sans-serif;position:relative}

  .card{position:absolute;left:150px;width:900px;height:515px;border-radius:36px;overflow:hidden}
  .card--front{top:50px;background:var(--card-white)}
  .card--back{top:635px;background:var(--brand-purple)}

  /* front */
  .front-name{position:absolute;left:64px;top:120px;width:320px;font-weight:700;font-size:46px;line-height:1.05;color:var(--brand-purple)}
  .front-art{position:absolute;left:420px;top:50px;width:450px;height:240px;border-radius:24px;
    background:linear-gradient(90deg,var(--bubble-blue) 0%,#d8f2fd 50%,#cfe8a8 78%,var(--germ-green) 100%)}
  .foam-band{position:absolute;left:0;bottom:0;width:900px;height:250px}
  .contact-list{position:absolute;left:230px;top:355px;list-style:none;color:var(--brand-purple);font-weight:500;font-size:27px}
  .contact-list li{display:flex;align-items:center;gap:14px;height:42px}
  .contact-list svg{width:26px;height:26px;flex:none}

  /* back */
  .back-name{position:absolute;left:0;right:0;top:150px;text-align:center;font-weight:700;font-size:72px;line-height:1.05;color:var(--text-light)}
  .social-row{position:absolute;left:0;right:0;top:400px;display:flex;justify-content:center;align-items:center;gap:22px;color:var(--text-light);font-weight:500;font-size:26px}
  .social-item{display:flex;align-items:center;gap:8px}
  .social-square{width:22px;height:22px;border:2px solid var(--accent-blue);border-radius:5px}
</style>
</head>
<body>

<section class="card card--front">
  <div class="front-name">Brightwell Surface Care</div>
  <div class="front-art" role="img" aria-label="Cartoon soap bubbles chasing a scared green mildew figure"></div>
  <svg class="foam-band" viewBox="0 0 900 250" preserveAspectRatio="none" aria-hidden="true">
    <path fill="var(--foam-blue)" d="M0 95 C90 40 210 45 300 90 C320 40 400 20 450 55 C500 15 590 25 610 110 C620 165 615 215 600 250 L0 250 Z"/>
  </svg>
  <ul class="contact-list">
    <li><svg viewBox="0 0 24 24"><path fill="currentColor" d="M6.6 10.8a15 15 0 0 0 6.6 6.6l2.2-2.2c.3-.3.7-.4 1-.2 1.1.4 2.3.6 3.6.6.6 0 1 .4 1 1V20c0 .6-.4 1-1 1A17 17 0 0 1 3 4c0-.6.4-1 1-1h3.5c.6 0 1 .4 1 1 0 1.3.2 2.5.6 3.6.1.3 0 .7-.2 1z"/></svg>(000) 000 0000</li>
    <li><svg viewBox="0 0 24 24"><path fill="currentColor" d="M2 5h20v14H2z"/><path fill="none" stroke="#fff" stroke-width="1.6" d="M2 5l10 8 10-8"/></svg>email@youremail.com</li>
    <li><svg viewBox="0 0 24 24" fill="none" stroke="currentColor" stroke-width="2"><circle cx="12" cy="12" r="10"/><path d="M2 12h20M12 2c3 3 3 17 0 20M12 2c-3 3-3 17 0 20"/></svg>www.yourwebsite.com</li>
  </ul>
</section>

<section class="card card--back">
  <div class="back-name">Brightwell<br>Surface Care</div>
  <div class="social-row">
    <span class="social-item"><span class="social-square"></span>Pixelvine</span>
    <span class="social-item"><span class="social-square"></span>Mingleport</span>
    <span>@brightwellsurfacecare</span>
  </div>
</section>

</body>
</html>
```